Security Warning Sign

We have an existing sign that needs an update. I have attached a picture of the current square sign. We need to maintain the same wording. It needs to be professional and appropriate to attach to our customers fence. Also attached is a copy of our building sign which may lend some inspiration and hopefully the ai format will assist. The final sign will be 600mm x 600mmOur website is www.halvorngate.com.au

```html
<!DOCTYPE html>
<html lang="en">
<head>
<meta charset="utf-8">
<title>Security Warning Sign</title>
<link rel="stylesheet" href="https://fonts.googleapis.com/css2?family=Roboto:wght@500;900&family=Open+Sans:wght@800&display=swap">
<style>
  :root {
    --sign-orange: #f5841f;
    --sign-dark: #232425;
    --sign-dark-soft: #2c2d2e;
    --panel-white: #ffffff;
    --ink: #1a1c1c;
    --stripe-grey: #4a4b4c;
    --text-light: #ffffff;
  }
  html, body {
    margin: 0;
    padding: 0;
    width: 1200px;
    height: 1199px;
    overflow: hidden;
    background: var(--sign-dark);
  }
  .sign {
    display: block;
    width: 1200px;
    height: 1199px;
  }
  .headline {
    font-family: "Roboto", Arial, sans-serif;
    font-weight: 900;
    fill: var(--sign-orange);
  }
  .notice-line {
    font-family: "Roboto", Arial, sans-serif;
    font-weight: 500;
    font-size: 94px;
    fill: var(--ink);
  }
  .company-name {
    font-family: "Open Sans", Arial, sans-serif;
    font-weight: 800;
    font-size: 49px;
    fill: var(--text-light);
  }
  .phone-number {
    font-family: "Open Sans", Arial, sans-serif;
    font-weight: 800;
    font-size: 56px;
    fill: var(--text-light);
  }
  .website {
    font-family: "Open Sans", Arial, sans-serif;
    font-weight: 800;
    font-size: 37px;
    fill: var(--text-light);
  }
</style>
</head>
<body>
<svg class="sign" viewBox="0 0 1200 1199" xmlns="http://www.w3.org/2000/svg">
  <defs>
    <linearGradient id="backdrop" x1="0" y1="0" x2="1" y2="1">
      <stop offset="0" stop-color="#2a2b2c"/>
      <stop offset="0.5" stop-color="#222324"/>
      <stop offset="1" stop-color="#262728"/>
    </linearGradient>
    <radialGradient id="cameraTones" cx="0.5" cy="0.4" r="0.6">
      <stop offset="0" stop-color="#f2f2f2"/>
      <stop offset="0.55" stop-color="#c9cacc"/>
      <stop offset="1" stop-color="#3a3d45"/>
    </radialGradient>
  </defs>

  <rect class="backdrop" width="1200" height="1199" fill="url(#backdrop)"/>

  <text class="headline" x="113" y="233" font-size="222" textLength="969" lengthAdjust="spacingAndGlyphs">WARNING</text>

  <polygon class="notice-panel" points="352,280 1110,280 1110,922 90,922 90,543" fill="var(--panel-white)"/>

  <circle class="camera-badge" cx="219" cy="409" r="148" fill="var(--sign-orange)"/>
  <circle class="camera-photo" cx="219" cy="412" r="112" fill="url(#cameraTones)" role="img" aria-label="Photo of a white dome security camera"/>

  <g class="notice-text" text-anchor="end">
    <text class="notice-line" x="1026" y="423" textLength="530" lengthAdjust="spacingAndGlyphs">ELECTRONIC</text>
    <text class="notice-line" x="1026" y="530" textLength="645" lengthAdjust="spacingAndGlyphs">SURVEILLANCE</text>
    <text class="notice-line" x="1026" y="639" textLength="709" lengthAdjust="spacingAndGlyphs">AND RECORDING</text>
    <text class="notice-line" x="1026" y="746" textLength="853" lengthAdjust="spacingAndGlyphs">DEVICES INSTALLED</text>
    <text class="notice-line" x="1026" y="855" textLength="571" lengthAdjust="spacingAndGlyphs">IN THIS AREA</text>
  </g>

  <g class="company-block">
    <circle class="company-dot" cx="182" cy="1028" r="78" fill="var(--sign-orange)"/>
    <text class="company-name" x="286" y="1019" textLength="288" lengthAdjust="spacingAndGlyphs">HALVORNGATE</text>
    <text class="company-name" x="286" y="1064" textLength="218" lengthAdjust="spacingAndGlyphs">SECURITY</text>
    <text class="company-name" x="286" y="1107" textLength="211" lengthAdjust="spacingAndGlyphs">SERVICES</text>
  </g>

  <g class="phone-bar">
    <polygon class="phone-stripe" points="688,1008 702,1008 652,1075 638,1075" fill="var(--stripe-grey)"/>
    <polygon class="phone-band" points="716,988 1105,988 1105,1075 674,1075" fill="var(--sign-orange)"/>
    <path class="phone-icon" d="M733 1018 c4 -4 9 -4 12 0 l6 8 c2 3 1 7 -2 9 l-4 3 c3 7 8 12 15 15 l3 -4 c2 -3 6 -4 9 -2 l8 6 c4 3 4 8 0 12 l-4 4 c-5 5 -14 5 -24 -1 c-10 -6 -19 -15 -25 -25 c-6 -10 -6 -19 -1 -24 z" fill="var(--sign-dark)"/>
    <text class="phone-number" x="779" y="1048" textLength="286" lengthAdjust="spacingAndGlyphs">1300 555 014</text>
  </g>

  <text class="website" x="600" y="1149" text-anchor="middle">WWW.HALVORNGATE.COM.AU</text>
</svg>
</body>
</html>
```